Book cover for publishing doctoral research about various national styles of piano playing.

I need a book cover for a publication of a doctoral research with regard to styles of piano performance characteristic to various nations.

Any images or graphics are optional, typography seems most important, but please feel free to be creative.

I attach the barcode, qsr and publisher's logo in the next few days. (Logo is still being designed).

For various reasons the size of the book is not completely decided yet. Please create your design in 7" x 10", but if at all possible, I would like to ask for files of two sizes, also including 8.5" x 11" in the final submission.

I am looking for a design that looks professional, probably simple, but I am open to any suggestions.
Updates

Dear Designers,I would like to thank you all for participation and submitting so many high-quality designs.My final decision was based on the feedback I received from my professional colleagues and potential readers.I would like to wish you all the best for the future.Best wishes,Radosław Added Monday, December 21, 2015

Target Market(s)

Pianists, students, music professionals

Industry/Entity Type

Publishing

Requirements
Must have
• Title: Tracing Regional Keyboard Lineages
• Subtitle: Origins and legacies
• Author: Radosław Kępiński
• Space for my logo on the front page and the spine.
• On the back page, please include some space for a short biography, 'barcode' and 'qsr' code.
• Please include whatever else you consider necessary.
Nice to have
• Would it be possible to use the same cover to a e-book edition?

```html
<!DOCTYPE html>
<html lang="en">
<head>
<meta charset="utf-8">
<title>Tracing Regional Keyboard Lineages – Cover Wrap</title>
<link href="https://fonts.googleapis.com/css2?family=Montserrat:wght@300;400;700;800&family=Roboto+Condensed:wght@400&family=Lato:wght@400&display=swap" rel="stylesheet">
<style>
  :root {
    --stage: #e9e9e9;
    --ink: #161616;
    --red: #e2262b;
    --white: #ffffff;
    --body-text: #d6d6d6;
    --photo-light: #e4e4e4;
    --photo-mid: #a9a9a9;
    --photo-dark: #2a2a2a;
  }
  * { box-sizing: border-box; margin: 0; padding: 0; }
  html, body { width: 1200px; height: 1200px; overflow: hidden; }
  body { background: var(--stage); position: relative; font-family: "Montserrat", sans-serif; }

  .cover-wrap {
    position: absolute; left: 50px; top: 224px;
    width: 1100px; height: 752px;
    display: grid; grid-template-columns: 525px 50px 525px;
    background: var(--ink);
    box-shadow: 0 10px 30px rgba(0,0,0,.25);
  }
  .panel { position: relative; overflow: hidden; }

  /* Back cover */
  .back-photo {
    position: absolute; left: 0; top: 0; width: 100%; height: 281px;
    background: linear-gradient(180deg, var(--photo-mid) 0%, var(--photo-light) 45%, #f4f4f4 100%);
  }
  .bio { position: absolute; left: 40px; top: 318px; width: 450px; height: 276px; overflow: hidden; }
  .bio-heading {
    color: var(--red); font-size: 12px; font-weight: 400; letter-spacing: 3px; margin-bottom: 7px;
  }
  .bio p {
    font-family: "Lato", sans-serif; color: var(--body-text);
    font-size: 9px; line-height: 1.4; margin-bottom: 9px;
  }
  .back-title { position: absolute; left: 40px; top: 618px; width: 445px; }
  .back-title .title-line { font-size: 18px; color: var(--white); font-weight: 300; letter-spacing: -0.3px; }
  .back-title .rule { height: 1px; background: var(--red); margin: 3px 0 5px; width: 100%; }
  .back-title .byline { position: absolute; right: 0; top: 9px; font-size: 8px; color: var(--white); }
  .subtitle {
    font-family: "Roboto Condensed", sans-serif; text-transform: uppercase; color: var(--white);
    letter-spacing: 3px; font-size: 9px;
  }
  .barcode-space {
    position: absolute; left: 370px; top: 680px; width: 125px; height: 48px; background: var(--white);
  }
  .strong-red { color: var(--red); font-weight: 800; letter-spacing: -0.5px; }
  .byline b { font-weight: 800; letter-spacing: 2px; }
  .surname-red { color: var(--red); }

  /* Spine */
  .spine { background: var(--ink); }
  .spine-text {
    position: absolute; left: 50%; transform: translateX(-50%);
    writing-mode: vertical-rl; white-space: nowrap;
  }
  .spine-title { top: 70px; font-size: 14px; color: var(--white); font-weight: 300; }
  .spine-sub { top: 70px; left: 12px; transform: none; font-size: 6px; letter-spacing: 1.5px; color: var(--body-text); font-family: "Roboto Condensed", sans-serif; text-transform: uppercase; }
  .spine-author { top: 500px; font-size: 9px; color: var(--white); letter-spacing: 1px; }
  .spine-author .light { color: var(--red); letter-spacing: 2px; }

  /* Front cover */
  .front-photo {
    position: absolute; left: 0; top: 150px; width: 100%; height: 553px;
    background: radial-gradient(ellipse at 45% 45%, #4a4a4a 0%, var(--photo-dark) 40%, var(--ink) 80%);
  }
  .front-title { position: absolute; left: 36px; top: 52px; width: 420px; }
  .front-title .title-line {
    font-size: 33px; line-height: 1.1; color: var(--white); font-weight: 300; letter-spacing: -0.8px;
  }
  .front-title .rule { height: 2px; background: var(--red); width: 100%; margin: 6px 0 8px; }
  .front-title .subtitle { font-size: 10px; letter-spacing: 4px; }

  .author-band {
    position: absolute; left: -50px; right: 0; top: 703px; height: 24px; background: var(--red);
  }
  .author-band .byline {
    position: absolute; left: 320px; top: 4px; font-size: 11px; color: var(--white); letter-spacing: 2px;
  }
  .author-band .byline span { font-weight: 300; letter-spacing: 3px; }
  .author-band .by { font-size: 8px; font-weight: 700; }
</style>
</head>
<body>
  <main class="cover-wrap">
    <section class="panel back-cover">
      <div class="back-photo" role="img" aria-label="Black and white photograph of a grand piano on an empty orchestra stage with chairs and music stands"></div>
      <div class="bio">
        <h2 class="bio-heading">BIOGRAPHY</h2>
        <p>Lorem ipsum dolor sit amet, consectetur adipiscing elit. Nullam convallis nec eros vitae faucibus. Cum sociis natoque penatibus et magnis dis parturient montes, nascetur ridiculus mus. Fusce nec nisl non erat dictum lobortis. Duis sed ullamcorper ligula. Proin et diam in turpis interdum commodo at eu lacus. Nunc rhoncus magna erat, sit amet posuere lorem lobortis et. Ut in tortor condimentum, efficitur mi et, pretium tellus. In neque enim, tempor id eros ac, tristique dictum leo.</p>
        <p>Nullam congue urna libero, eu porttitor lectus dictum sed. Duis aliquam faucibus sem sed posuere. Donec congue, tortor at dapibus blandit, nisi dui aliquam mauris, ac dapibus metus magna quis nunc. Integer tempor sed eros ut consequat. Sed convallis sem sollicitudin massa varius, gravida volutpat elit tristique. Class aptent taciti sociosqu ad litora torquent per conubia nostra, per inceptos himenaeos. Sed et iaculis quam. Donec lacinia tellus nulla, vitae tincidunt ligula hendrerit eu. Fusce malesuada dignissim dictum. Sed tincidunt turpis nisl, eu pretium lorem vulputate sit amet. Vivamus lacinia dolor ac est tincidunt, condimentum ex mattis.</p>
        <p>Vestibulum pulvinar vitae sem quis convallis. Pellentesque congue justo ut est ultrices molestie. Donec ac dui dictum, pulvinar neque porta, mollis lorem. Morbi consectetur efficitur lectus, vel aliquam tortor placerat et. Nunc orci sem, eleifend ac libero nec, blandit fringilla massa. Nullam auctor diam ac nulla varius elementum. Aenean dapibus maximus sem, at condimentum elit fringilla sit amet. Curabitur rhoncus eu purus quis efficitur. Aenean iaculis est eget neque elementum, at placerat magna vehicula. Nullam id egestas nunc, ac pharetra orci. Aenean sagittis porta libero, at placerat magna accumsan in.</p>
      </div>
      <div class="back-title">
        <div class="title-line"><span class="strong-red">TRACING</span> REGIONAL</div>
        <div class="byline">by <b>RADOSŁAW</b> <span class="surname-red">KĘPIŃSKI</span></div>
        <div class="rule"></div>
        <div class="subtitle">Origins and legacies</div>
      </div>
      <div class="barcode-space"></div>
    </section>

    <section class="panel spine">
      <div class="spine-text spine-title"><span class="strong-red">TRACING</span> REGIONAL KEYBOARD LINEAGES</div>
      <div class="spine-text spine-sub">Origins and legacies</div>
      <div class="spine-text spine-author">by <b>RADOSŁAW</b> <span class="light">KĘPIŃSKI</span></div>
    </section>

    <section class="panel front-cover" style="overflow:visible">
      <div class="front-photo" role="img" aria-label="Black and white photograph of a pianist in a dark suit seen from behind, playing a grand piano"></div>
      <div class="front-title">
        <div class="title-line"><span class="strong-red">TRACING</span> REGIONAL</div>
        <div class="title-line">KEYBOARD LINEAGES</div>
        <div class="rule"></div>
        <div class="subtitle">Origins and legacies</div>
      </div>
      <div class="author-band">
        <div class="byline"><span class="by">by</span> <b>RADOSŁAW</b> <span>KĘPIŃSKI</span></div>
      </div>
    </section>
  </main>
</body>
</html>
```